Dr. Lumora needs a design for its website!

*Only need the design, coding is not required.
*Need desktop version ($500) and mobile/tablet version ($200)
*The attached files are not the exact layout we want, they are just for you to know what information should be included in those pages.
*The function of our website is like www.qavlo.hk
*For the background picture, prefer a lively picture and chinese people in it, NOT necessarily need a doctor or sick person in the picture

***Don't just copy the layout from the attachments or from the reference website, we are looking for creative ideas, non-ordinary designs!!!****

We are developing a website for the public to search a doctor by different criteria. At the initial stage, we need 4 pages to start with and other pages at later stage. I have attached the general idea of these pages but not necessarily to be exactly the same, I am looking for some new ideas.

This website needs a professional, modern, simple and user friendly design. The main color to be used in the website will be same as the color (R:0 G:139 B:205) used in our logo (see attached). We don't have any particular thoughts for the other color and the font to be used in the website. Can try to use circle outline for the icon in the navigation bar.

1. Home: will include 4 sections (see attached)

2. Doctor's details (see attached)

3. Health information: will include a short descriptions of this Health Info page and 5 sections (see attached)

4. News (see attached)

Reason: Not too many suitable designs to choose from and need more time to go through the designs

All

Medical

4 page

• must not be same as or looks too much like www.qavlo.hk
• prefer not to use black and red color

```html
<!DOCTYPE html>
<html lang="en">
<head>
<meta charset="utf-8">
<title>Dr. Lumora – Find a Doctor</title>
<link rel="stylesheet" href="https://fonts.googleapis.com/css2?family=Titillium+Web:wght@300;400&family=Oswald:wght@400;500&family=Noto+Sans+TC:wght@500&display=swap">
<style>
:root{
  --brand:#008bcd;
  --brand-deep:#0a7fc0;
  --band:#078ccd;
  --ink:#333;
  --ink-soft:#444;
  --row-alt:#c4c4c4;
  --white:#fff;
  --field-line:#5a6670;
}
*{box-sizing:border-box;margin:0;padding:0}
html,body{width:1200px;height:899px;overflow:hidden;background:var(--white)}
body{position:relative;font-family:"Titillium Web",sans-serif;font-weight:300;color:var(--ink)}
.abs{position:absolute;white-space:nowrap}

/* header */
.brand{left:222px;top:14px;display:flex;align-items:center;gap:8px}
.brand-dot{width:38px;height:38px;border-radius:50%;background:var(--brand)}
.brand-name{font-size:26px;font-weight:400;color:var(--brand);line-height:1}
.langs{right:236px;top:27px;font-size:15px;font-weight:300;color:var(--ink);font-family:"Titillium Web","Noto Sans TC",sans-serif}

.nav-band{left:0;top:76px;width:1200px;height:44px;
  background:linear-gradient(#fff 0%,#9fd0ec 45%,#1e88c8 100%);
  box-shadow:0 3px 3px rgba(0,0,0,.45)}
.nav-item{top:88px;font-size:16px;color:var(--ink)}
.nav-home{left:224px;top:82px;width:64px;height:32px;background:#fff;border-radius:5px;
  color:var(--brand);font-size:16px;text-align:center;line-height:32px}
.search-box{left:826px;top:90px;width:156px;height:19px;background:#fff;border-radius:10px;
  display:flex;align-items:center;gap:4px;padding-left:6px;font-size:11px;color:#888;font-weight:400}

/* panels */
.panel{background:linear-gradient(#fff 0%,#9fd3ef 45%,#1b8dd0 100%);
  box-shadow:0 3px 4px rgba(0,0,0,.5)}
.finder{left:224px;top:136px;width:300px;height:386px}
.login{left:554px;top:136px;width:417px;height:192px}
.perks{left:554px;top:338px;width:417px;height:184px}

.label{font-size:19px;color:var(--ink-soft)}
.field{background:#fff;border:1px solid var(--field-line);border-radius:8px}
.select::after{content:"";position:absolute;right:8px;top:11px;border-left:10px solid transparent;
  border-right:10px solid transparent;border-top:6px solid #333}
.radio{width:15px;height:15px;border:1.4px solid #555;border-radius:50%;background:#fff}
.btn{background:#fff;border-radius:4px;color:var(--brand);font-size:16px;font-weight:400;
  display:flex;align-items:center;justify-content:center;gap:4px}

.panel-title{font-size:24px;color:var(--ink-soft);text-align:center;width:417px;left:554px}
.forgot{left:685px;top:281px;font-size:19px;color:var(--ink-soft);text-decoration:underline}
.perk{left:590px;font-size:17px;color:var(--ink-soft);display:flex;align-items:center;gap:10px}
.perk-more{left:639px;top:494px;font-size:17px;color:var(--ink-soft)}

/* results table */
.results{left:216px;top:543px;width:767px;height:215px;background:var(--brand);border-radius:6px;
  box-shadow:0 4px 4px rgba(0,0,0,.5)}
.th{top:558px;font-family:"Oswald","Noto Sans TC",sans-serif;font-weight:500;font-size:20px;color:#fff;
  transform:scaleX(.88);transform-origin:left}
.th.cjk{font-family:"Noto Sans TC",sans-serif;font-size:19px;transform:none;top:561px}
.rows{left:224px;top:595px;width:752px;height:154px;overflow:hidden}
.row{height:38.5px;position:relative;font-family:"Oswald",sans-serif;font-size:17px;color:#222}
.row:nth-child(even){background:var(--row-alt)}
.row:nth-child(odd){background:#fff}
.row span{position:absolute;top:7px;white-space:nowrap;line-height:1.4;transform:scaleX(.85);transform-origin:left}

/* social */
.social{left:224px;top:776px;width:752px;height:69px;background:var(--brand);border-radius:5px}
.soc-dot{width:46px;height:46px;border-radius:50%;background:#fff;top:789px}
.soc-name{top:796px;font-size:19px;color:#fff}

.foot{left:0;top:859px;width:1200px;height:40px;background:var(--band)}
</style>
</head>
<body>

<header>
  <div class="abs brand"><span class="brand-dot"></span><span class="brand-name">Dr. Lumora</span></div>
  <div class="abs langs">English | 한국어 | 日本語</div>
</header>

<nav>
  <div class="abs nav-band"></div>
  <div class="abs nav-home">Home</div>
  <div class="abs nav-item" style="left:349px">TBC</div>
  <div class="abs nav-item" style="left:430px">Health Info</div>
  <div class="abs nav-item" style="left:552px">News</div>
  <div class="abs nav-item" style="left:646px">About Us</div>
  <div class="abs nav-item" style="left:745px">Contact Us</div>
  <div class="abs search-box">
    <svg width="12" height="12" viewBox="0 0 12 12"><circle cx="5" cy="5" r="3.6" fill="none" stroke="#888" stroke-width="1.2"/><line x1="7.6" y1="7.6" x2="11" y2="11" stroke="#888" stroke-width="1.4"/></svg>Search
  </div>
</nav>

<section class="abs panel finder" aria-label="Doctor search"></section>
<div class="abs label" style="left:233px;top:140px">Doctor’s name:</div>
<div class="abs field" style="left:354px;top:139px;width:160px;height:29px"></div>
<div class="abs label" style="left:233px;top:190px">Gender:</div>
<div class="abs radio" style="left:327px;top:197px"></div>
<div class="abs label" style="left:353px;top:190px">Male</div>
<div class="abs radio" style="left:427px;top:197px"></div>
<div class="abs label" style="left:452px;top:190px">Female</div>
<div class="abs label" style="left:233px;top:245px">Specialism:</div>
<div class="abs field select" style="left:326px;top:244px;width:188px;height:29px"></div>
<div class="abs label" style="left:233px;top:302px">Symptoms:</div>
<div class="abs field select" style="left:326px;top:302px;width:188px;height:29px"></div>
<div class="abs label" style="left:233px;top:361px">District:</div>
<div class="abs field select" style="left:326px;top:361px;width:188px;height:29px"></div>
<div class="abs label" style="left:233px;top:419px">Phone Number</div>
<div class="abs field" style="left:358px;top:418px;width:156px;height:29px"></div>
<div class="abs btn" style="left:327px;top:471px;width:72px;height:25px">Reset</div>
<div class="abs btn" style="left:432px;top:471px;width:74px;height:25px">Search
  <svg width="14" height="14" viewBox="0 0 14 14"><circle cx="6" cy="6" r="4.3" fill="none" stroke="#008bcd" stroke-width="1.4"/><line x1="9" y1="9" x2="13" y2="13" stroke="#008bcd" stroke-width="1.6"/></svg>
</div>

<section class="abs panel login" aria-label="Member login"></section>
<div class="abs panel-title" style="top:144px">Member login</div>
<div class="abs label" style="left:562px;top:186px">Login Email:</div>
<div class="abs field" style="left:671px;top:188px;width:291px;height:27px"></div>
<div class="abs label" style="left:562px;top:237px">Password:</div>
<div class="abs field" style="left:671px;top:238px;width:291px;height:27px"></div>
<div class="abs forgot">Forgot password</div>
<div class="abs btn" style="left:870px;top:282px;width:73px;height:25px">Login in</div>

<section class="abs panel perks" aria-label="Membership benefits"></section>
<div class="abs panel-title" style="top:338px">Become a Dr. Lumora Member</div>
<div class="abs perk" style="top:374px"><svg width="18" height="16" viewBox="0 0 18 16"><path d="M1 9 L6 14 L17 1" fill="none" stroke="#444" stroke-width="2.6"/></svg>First-hands health news</div>
<div class="abs perk" style="top:398px"><svg width="18" height="16" viewBox="0 0 18 16"><path d="M1 9 L6 14 L17 1" fill="none" stroke="#444" stroke-width="2.6"/></svg>Exclusive promotions</div>
<div class="abs perk" style="top:422px"><svg width="18" height="16" viewBox="0 0 18 16"><path d="M1 9 L6 14 L17 1" fill="none" stroke="#444" stroke-width="2.6"/></svg>Instant health advices</div>
<div class="abs perk" style="top:446px"><svg width="18" height="16" viewBox="0 0 18 16"><path d="M1 9 L6 14 L17 1" fill="none" stroke="#444" stroke-width="2.6"/></svg>Free health Seminars/talks</div>
<div class="abs perk" style="top:470px"><svg width="18" height="16" viewBox="0 0 18 16"><path d="M1 9 L6 14 L17 1" fill="none" stroke="#444" stroke-width="2.6"/></svg>Prioritary doctor oppointments</div>
<div class="abs perk-more">and more!</div>

<section class="abs results" aria-label="Search results"></section>
<div class="abs th" style="left:238px">Name</div>
<div class="abs th" style="left:295px">Gender</div>
<div class="abs th" style="left:382px">Specialism</div>
<div class="abs th cjk" style="left:497px">執業簡介</div>
<div class="abs th cjk" style="left:613px">醫務所地址</div>
<div class="abs th" style="left:727px">Address</div>
<div class="abs th" style="left:814px">District</div>
<div class="abs th" style="left:900px">Phone No.</div>
<div class="abs rows">
  <div class="row"><span style="left:14px">XXXXX</span><span style="left:82px">XXX</span><span style="left:178px">XXXXX</span><span style="left:273px">XXXXXXX</span><span style="left:417px">XXXXX</span><span style="left:513px">XXXXX</span><span style="left:596px">XXXXX</span><span style="left:676px">3456-78901</span></div>
  <div class="row"><span style="left:14px">XXXXX</span><span style="left:82px">XXX</span><span style="left:178px">XXXXX</span><span style="left:273px">XXXXXXX</span><span style="left:417px">XXXXX</span><span style="left:513px">XXXXX</span><span style="left:596px">XXXXX</span><span style="left:676px">3456-78901</span></div>
  <div class="row"><span style="left:14px">XXXXX</span><span style="left:82px">XXX</span><span style="left:178px">XXXXX</span><span style="left:273px">XXXXXXX</span><span style="left:417px">XXXXX</span><span style="left:513px">XXXXX</span><span style="left:596px">XXXXX</span><span style="left:676px">3456-78901</span></div>
  <div class="row"><span style="left:14px">XXXXX</span><span style="left:82px">XXX</span><span style="left:178px">XXXXX</span><span style="left:273px">XXXXXXX</span><span style="left:417px">XXXXX</span><span style="left:513px">XXXXX</span><span style="left:596px">XXXXX</span><span style="left:676px">3456-78901</span></div>
</div>

<section class="abs social" aria-label="Social links"></section>
<div class="abs soc-dot" style="left:256px"></div><div class="abs soc-name" style="left:318px">Searchly</div>
<div class="abs soc-dot" style="left:449px"></div><div class="abs soc-name" style="left:508px">Circlebook</div>
<div class="abs soc-dot" style="left:655px"></div><div class="abs soc-name" style="left:714px">Chirper</div>
<div class="abs soc-dot" style="left:820px"></div><div class="abs soc-name" style="left:882px">Viewtube</div>

<footer class="abs foot"></footer>
</body>
</html>
```